Business Card needed for Drainor, a growing Septic Service company

Drainor, a growing local septic service company in Pennsylvania, needs updated business cards. We'd like the business card to feature our logo and communicate that we provide Septic Pumping, Installations/Repairs, Restroom Rentals, and 24/7 Emergency Service. The business card should be eye-catching, bold, and clean/simple. We have been in business almost 10 years and would like to expand and update our business brand and image.

Target Market(s)

Residential and Commercial, New and Current Homeowners

Industry/Entity Type

Service

Contact Information for Business Card

Contact on the business card should be: Dean Harlow Owner & Operator
Phone: 610-555-0187
Email: service@drainor-example.com
Website: www.drainor-example.com
Address: 812 Millbrook Lane Brookvale PA 18999

Font styles to use
Sans Serif

Colors

Designer to choose colors to be used in the design.

Requirements
Must have
• Feature logo on both side of business card.
Nice to have
• We envision the contact information on one side and our services listed on the other side. Utilize the green from the symbol in our logo as part of the design, overall design color scheme should be white, grey, black.

```html
<!DOCTYPE html>
<html lang="en">
<head>
<meta charset="utf-8">
<title>Drainor Business Card</title>
<link rel="stylesheet" href="https://fonts.googleapis.com/css2?family=Arimo:ital,wght@0,400;0,700;1,400&family=Montserrat:wght@800&display=swap">
<style>
  :root {
    --green: #86c440;
    --black: #0d0d0d;
    --white: #ffffff;
    --grey-bg: #d9d9da;
    --grey-tab: #8a8a8a;
  }
  * { box-sizing: border-box; margin: 0; padding: 0; }
  html, body { width: 1200px; height: 1200px; overflow: hidden; }
  body { background: var(--grey-bg); position: relative; font-family: "Arimo", Arial, sans-serif; }

  .card-slot { position: absolute; left: 180px; width: 840px; height: 478px; }
  .card-slot--front { top: 90px; }
  .card-slot--back { top: 624px; }

  .card {
    position: absolute; left: 0; top: 0;
    width: 700px; height: 398px;
    transform: scale(1.2); transform-origin: 0 0;
    overflow: hidden; background: var(--white);
    box-shadow: 0 3px 10px rgba(0,0,0,0.18);
  }
  .block { position: absolute; }

  .brand {
    position: absolute; display: flex; align-items: center;
    background: var(--white);
  }
  .brand__square { background: var(--green); flex: none; }
  .brand__name {
    font-family: "Montserrat", Arial, sans-serif; font-weight: 800;
    color: var(--black); letter-spacing: 2px; line-height: 1;
  }

  .site-url {
    position: absolute; left: 0; width: 700px; height: 53px;
    display: flex; align-items: center; justify-content: center;
    font-family: "Montserrat", Arial, sans-serif; font-weight: 800;
    font-size: 20px; letter-spacing: 1px;
  }

  /* Front */
  .front__green { left: 350px; top: 0; width: 350px; height: 345px; background: var(--green); }
  .front .brand { left: 147px; top: 43px; width: 450px; height: 92px; padding-left: 5px; }
  .front .brand__square { width: 70px; height: 70px; margin-right: 14px; }
  .front .brand__name { font-size: 52px; }
  .front .site-url { top: 345px; background: var(--black); color: var(--white); }

  .person { position: absolute; left: 0; top: 213px; height: 50px; padding-left: 19px; }
  .person::before { content: ""; position: absolute; left: 0; top: 0; width: 10px; height: 50px; background: var(--green); }
  .person__name { font-weight: 700; font-size: 25px; color: var(--black); line-height: 1.05; }
  .person__role { font-style: italic; font-size: 17.5px; color: var(--black); margin-top: 3px; }

  .tab { position: absolute; }
  .front .tab { left: 340px; top: 178px; }

  .contact-list { position: absolute; left: 375px; top: 194px; list-style: none; color: var(--white); font-size: 20.5px; line-height: 27.5px; }

  /* Back */
  .back__green { left: 0; top: 0; width: 350px; height: 345px; background: var(--green); }
  .back__black { left: 350px; top: 0; width: 350px; height: 345px; background: var(--black); }
  .back .brand { left: 0; top: 45px; width: 350px; height: 122px; padding-left: 17px; }
  .back .brand__square { width: 55px; height: 57px; margin-right: 10px; }
  .back .brand__name { font-size: 40px; letter-spacing: 1.5px; }
  .back .site-url { top: 345px; background: var(--white); color: var(--black); }
  .back .tab { left: 340px; top: 183px; }

  .service-list { position: absolute; left: 377px; top: 204px; list-style: none; color: var(--white); font-size: 20.5px; line-height: 25px; }
  .service-list__accent { color: var(--green); font-weight: 700; }
</style>
</head>
<body>

<div class="card-slot card-slot--front">
  <section class="card front" aria-label="Business card front">
    <div class="block front__green"></div>
    <div class="brand">
      <span class="brand__square"></span>
      <span class="brand__name">DRAINOR</span>
    </div>

    <div class="person">
      <p class="person__name">DEAN HARLOW</p>
      <p class="person__role">Owner &amp; Operator</p>
    </div>

    <svg class="tab" width="24" height="120" viewBox="0 0 24 120" aria-hidden="true">
      <polygon points="10,0 24,8 24,112 10,120" fill="var(--grey-tab)"/>
      <polygon points="0,6 12,0 22,6 22,114 12,120 0,114" fill="var(--black)"/>
      <g fill="none" stroke="var(--white)" stroke-width="1.4">
        <path d="M7 24 q0 8 8 9 l1.5 -2.5 l-3 -2 l-1.5 1.5 q-2.5 -1 -3 -3 l1.5 -1.5 l-2 -3 z" fill="var(--white)" stroke="none"/>
        <rect x="5.5" y="51" width="11" height="8"/>
        <path d="M5.5 51 l5.5 4.5 l5.5 -4.5"/>
      </g>
      <path d="M11 74 a4.5 4.5 0 0 1 4.5 4.5 q0 3 -4.5 8.5 q-4.5 -5.5 -4.5 -8.5 A4.5 4.5 0 0 1 11 74 z M11 76.8 a1.7 1.7 0 1 0 0.01 0 z" fill="var(--white)" fill-rule="evenodd"/>
    </svg>

    <ul class="contact-list">
      <li>610-555-0187</li>
      <li>service@drainor-example.com</li>
      <li>812 Millbrook Lane</li>
      <li>Brookvale PA 18999</li>
    </ul>

    <div class="site-url">WWW.DRAINOR-EXAMPLE.COM</div>
  </section>
</div>

<div class="card-slot card-slot--back">
  <section class="card back" aria-label="Business card back">
    <div class="block back__green"></div>
    <div class="block back__black"></div>
    <div class="brand">
      <span class="brand__square"></span>
      <span class="brand__name">DRAINOR</span>
    </div>

    <svg class="tab" width="24" height="144" viewBox="0 0 24 144" aria-hidden="true">
      <polygon points="10,0 24,8 24,136 10,144" fill="var(--grey-tab)"/>
      <polygon points="0,6 12,0 22,6 22,138 12,144 0,138" fill="var(--white)"/>
      <g fill="var(--green)">
        <circle cx="11" cy="27" r="5"/>
        <circle cx="11" cy="52" r="5"/>
        <circle cx="11" cy="77" r="5"/>
        <circle cx="11" cy="102" r="5"/>
      </g>
    </svg>

    <ul class="service-list">
      <li>SEPTIC PUMPING</li>
      <li>INSTALLATIONS/ REPAIRS</li>
      <li>RESTROOM RENTALS</li>
      <li><span class="service-list__accent">24/7</span> EMERGENCY</li>
      <li>SERVICE</li>
    </ul>

    <div class="site-url">WWW.DRAINOR-EXAMPLE.COM</div>
  </section>
</div>

</body>
</html>
```